Looking for a professional, clean and crisp business card

I am in the underground utilities industry and am just looking for a really impressive business card. I would like our card to be white with our symbol crisp and clear with it protruding. I also have a business partner that will require his name and info on the card once the design is set. I would like to have our website info on the card which is;
http://granitetrenchco.example/

Contact Information for Business Card

Website, contact name, number and email

```html
<!DOCTYPE html>
<html lang="en">
<head>
<meta charset="utf-8">
<title>Granite Trench Co — Business Card</title>
<link rel="stylesheet" href="https://fonts.googleapis.com/css2?family=Montserrat:wght@400;600;700&display=swap">
<style>
  :root {
    --stage: #e9ebee;
    --card-white: #ffffff;
    --card-grey: #a7a7a7;
    --ink: #1d1f22;
    --muted: #8a8d91;
    --accent: #3b62ad;
    --rule: #1f2a36;
    --shadow: rgba(20, 30, 45, 0.18);
  }
  * { box-sizing: border-box; margin: 0; padding: 0; }
  html, body {
    width: 1200px; height: 913px; overflow: hidden;
    background: var(--stage);
    font-family: "Montserrat", sans-serif;
    color: var(--ink);
  }
  .canvas { position: relative; width: 1200px; height: 913px; }

  .card {
    position: absolute;
    width: 665px; height: 380px;
    border-radius: 22px;
    box-shadow: 0 10px 26px var(--shadow);
  }
  .card--back { left: 80px; top: 60px; background: var(--card-grey); }
  .card--front { left: 455px; top: 473px; background: var(--card-white); }

  .wordmark {
    position: absolute;
    display: flex; align-items: center; gap: 14px;
    font-weight: 700; color: var(--ink);
    letter-spacing: 0.5px; white-space: nowrap;
  }
  .wordmark__dot {
    width: 26px; height: 26px; border-radius: 50%;
    background: var(--ink); flex: none;
  }
  .card--back .wordmark {
    left: 50%; top: 50%; transform: translate(-50%, -50%);
    font-size: 38px;
  }
  .card--front .wordmark {
    left: 34px; top: 50%; transform: translateY(-50%);
    font-size: 21px;
  }
  .card--front .wordmark__dot { width: 18px; height: 18px; }

  .divider {
    position: absolute; left: 290px; top: 72px;
    width: 1.5px; height: 236px; background: var(--rule);
  }

  .contact { position: absolute; left: 322px; top: 86px; }
  .contact__name {
    font-size: 27px; font-weight: 700; letter-spacing: 1px;
    line-height: 1.1;
  }
  .contact__role {
    font-size: 15px; font-weight: 400; color: var(--muted);
    letter-spacing: 1.5px; margin-top: 4px;
  }
  .contact__list { list-style: none; margin-top: 34px; }
  .contact__item {
    display: flex; align-items: center; gap: 14px;
    font-size: 17px; font-weight: 400; line-height: 1;
    margin-bottom: 14px;
  }
  .contact__icon { width: 18px; height: 18px; flex: none; }
</style>
</head>
<body>
<main class="canvas">

  <section class="card card--back" aria-label="Card back">
    <div class="wordmark"><span class="wordmark__dot"></span>Granite Trench Co</div>
  </section>

  <section class="card card--front" aria-label="Card front">
    <div class="wordmark"><span class="wordmark__dot"></span>Granite Trench Co</div>
    <div class="divider"></div>

    <div class="contact">
      <h1 class="contact__name">DALE MORROW</h1>
      <p class="contact__role">OWNER</p>

      <ul class="contact__list">
        <li class="contact__item">
          <svg class="contact__icon" viewBox="0 0 24 24" aria-hidden="true">
            <path fill="var(--accent)" d="M6.6 10.8a15.1 15.1 0 0 0 6.6 6.6l2.2-2.2a1 1 0 0 1 1-.25 11.4 11.4 0 0 0 3.6.57 1 1 0 0 1 1 1V20a1 1 0 0 1-1 1A17 17 0 0 1 3 4a1 1 0 0 1 1-1h3.5a1 1 0 0 1 1 1c0 1.25.2 2.45.57 3.57a1 1 0 0 1-.25 1z"/>
          </svg>
          555-014-8736(DIGS)
        </li>
        <li class="contact__item">
          <svg class="contact__icon" viewBox="0 0 24 24" aria-hidden="true">
            <rect x="2" y="5" width="20" height="14" rx="1.5" fill="var(--accent)"/>
            <path d="M3 6.5l9 6.5 9-6.5" fill="none" stroke="#fff" stroke-width="1.6"/>
          </svg>
          dale@granitetrenchco.example
        </li>
        <li class="contact__item">
          <svg class="contact__icon" viewBox="0 0 24 24" aria-hidden="true">
            <circle cx="12" cy="12" r="10" fill="var(--accent)"/>
            <ellipse cx="12" cy="12" rx="4.2" ry="10" fill="none" stroke="#fff" stroke-width="1.3"/>
            <path d="M2 12h20M4 7h16M4 17h16" stroke="#fff" stroke-width="1.3"/>
          </svg>
          www.granitetrenchco.example
        </li>
      </ul>
    </div>
  </section>

</main>
</body>
</html>
```